Pricing Brochure Design Project for a Fish Farm

We need a pricing brochure design for a fish farm based in Haiti called Corvel Aquaculture S.A. We raise varies species of tilapia. Each of these species should have a corresponding pricing sheet. Additionally, we should have a pricing sheet for fillets and a separate one for fish carcasses. I have included a draft pricing brochure which contains all of the elements we are looking for as well as our logo.
Target Market(s)
Commercial Buyers (Hotels, Super Markets, Restaurants, etc.)
Industry/Entity Type
Farm
Requirements
Must have
- Please provide a separate sheet for each species of tilapia, one sheet for the tilapia fillets and one sheet for the fish carcasses. If you can find better images, please feel free to replace them.
The information sheet should have an image of the commercial grade cages (similar to the one pictured).
I have not located a suitable image for silver tilapia, but I am having images taken of our stock. If you are unable to locate an image of the silver tilapia, please provide a place holder.
Logo must be included

```html
<!DOCTYPE html>
<html lang="en">
<head>
<meta charset="utf-8">
<title>Corvel Poisson – Tilapia Pricing</title>
<link href="https://fonts.googleapis.com/css2?family=Questrial&display=swap" rel="stylesheet">
<style>
:root{
  --navy:#1a4a93;
  --navy-dark:#123a78;
  --green:#3cb54a;
  --green-light:#e6f5e4;
  --lavender:#e4e6f4;
  --paper:#ffffff;
  --ink:#1f2d4d;
  --bg:#eceae6;
}
*{box-sizing:border-box;margin:0;padding:0}
html,body{width:1200px;height:912px;overflow:hidden;background:var(--bg);font-family:"Questrial",sans-serif;color:var(--ink)}
.spread{position:absolute;left:20px;top:46px;width:1160px;height:820px;display:flex;box-shadow:0 6px 20px rgba(0,0,0,.18)}
.page{position:relative;width:580px;height:820px;background:var(--paper);overflow:hidden}
.page--left{border-right:1px solid #d8d8d8}
.band{position:absolute;left:0;width:580px;height:90px;display:block}
.band--top{top:0}
.band--bottom{bottom:0}
.brand{position:absolute;top:108px;display:flex;align-items:center;gap:8px;font-size:22px;color:var(--navy);letter-spacing:.5px}
.brand__dot{width:14px;height:14px;border-radius:50%;background:var(--green)}
.page--left .brand{left:44px}
.page--right .brand{right:44px}
.title-bar{position:absolute;height:58px;display:flex;align-items:center;color:#fff;font-size:28px;white-space:nowrap}
.title-bar__rule{width:3px;height:36px;background:#fff;margin:0 14px 0 20px;flex:none}
.fillets-title{left:0;top:250px;width:320px;background:var(--green)}
.fillet-notes{position:absolute;left:320px;top:205px;width:260px;height:80px;background:var(--navy);color:#fff;font-size:12px;padding:18px 20px;list-style:none;line-height:1.7}
.fillet-notes li::before{content:"";display:inline-block;width:5px;height:5px;background:#fff;margin-right:8px;vertical-align:middle}
.carcass-title{left:0;top:160px;width:270px;background:var(--navy);height:64px}
.carcass-bar{position:absolute;left:270px;top:150px;width:310px;height:54px;background:var(--green)}
.photo{position:absolute;box-shadow:0 3px 8px rgba(0,0,0,.3)}
.photo--fillet{left:125px;top:328px;width:320px;height:240px;border:4px solid var(--navy);background:linear-gradient(135deg,#3b3f44 0%,#c9d4dc 35%,#e98a6e 55%,#f3c2a8 70%,#2e3236 100%)}
.photo--carcass{left:140px;top:250px;width:300px;height:240px;border:4px solid var(--green);background:radial-gradient(ellipse at 50% 55%,#f4f2f0 0%,#e8b7ae 40%,#c8a27a 70%,#a07a52 100%)}
.pricing{position:absolute;border-collapse:collapse;font-size:11px;text-align:center}
.pricing th,.pricing td{border:1px solid #fff;padding:4px 6px;white-space:nowrap;line-height:1.2}
.pricing thead th{font-size:10px;font-weight:normal}
.pricing .cut{font-size:13px;text-align:left}
.pricing tbody th{text-align:left;font-weight:normal;font-size:10px}
.pricing--blue{left:110px;top:588px;width:440px}
.pricing--blue thead th{background:var(--navy);color:#fff}
.pricing--blue tbody th,.pricing--blue tbody td{background:var(--lavender)}
.pricing--green{left:120px;top:510px;width:440px}
.pricing--green thead th{background:var(--green);color:#fff}
.pricing--green tbody th,.pricing--green tbody td{background:var(--green-light)}
.folio{position:absolute;bottom:22px;color:#fff;font-size:13px;display:flex;align-items:center;gap:8px}
.page--left .folio{left:44px}
.page--right .folio{right:44px}
.folio svg{width:14px;height:14px}
</style>
</head>
<body>
<main class="spread">
  <section class="page page--left">
    <svg class="band band--top" viewBox="0 0 580 90" aria-hidden="true">
      <path d="M0 0H580V48H330C300 48 295 62 270 62H0Z" fill="var(--navy)"/>
      <path d="M0 70H270C295 70 300 56 330 56H580" fill="none" stroke="var(--green)" stroke-width="4"/>
    </svg>
    <div class="brand"><span class="brand__dot"></span>Corvel Poisson</div>
    <div class="title-bar fillets-title"><span class="title-bar__rule"></span>Tilapia Fillets</div>
    <ul class="fillet-notes">
      <li>5oz to 8oz per fillet</li>
      <li>Min Order for Delivery → 25 lbs</li>
    </ul>
    <div class="photo photo--fillet" role="img" aria-label="Photo of fresh tilapia fillets on ice and slate"></div>
    <table class="pricing pricing--blue">
      <thead>
        <tr><th class="cut" rowspan="2">CUT</th><th colspan="4">WEEKLY PRICING</th></tr>
        <tr><th>$/LB (1–50 lbs)</th><th>$/LB (51–150 lbs)</th><th>$/LB (151–250 lbs)</th><th>$/LB (+251 lbs)</th></tr>
      </thead>
      <tbody>
        <tr><th>Fillet (incl. skin)</th><td>5.00</td><td>4.50</td><td>4.25</td><td>4.00</td></tr>
        <tr><th>Fillet (skinless)</th><td>5.50</td><td>4.95</td><td>4.68</td><td>4.40</td></tr>
        <tr><th>Carcass (incl head)</th><td>0.50</td><td>0.45</td><td>0.43</td><td>0.40</td></tr>
      </tbody>
    </table>
    <svg class="band band--bottom" viewBox="0 0 580 90" aria-hidden="true">
      <path d="M0 90H580V28H330C300 28 295 14 270 14H0Z" fill="var(--navy)"/>
      <path d="M0 6H270C295 6 300 20 330 20H580" fill="none" stroke="var(--green)" stroke-width="4"/>
    </svg>
    <div class="folio"><span>6&nbsp;&nbsp;|</span>
      <svg viewBox="0 0 24 24" aria-hidden="true"><circle cx="12" cy="12" r="11" fill="none" stroke="#fff" stroke-width="2"/><path d="M8 6l3 3-2 2c1 2 2 3 4 4l2-2 3 3-2 2C10 18 6 14 6 8z" fill="#fff"/></svg>
      <span>509 2000 0147</span></div>
  </section>

  <section class="page page--right">
    <svg class="band band--top" viewBox="0 0 580 90" aria-hidden="true">
      <path d="M0 0H580V48H280C250 48 245 62 220 62H0Z" fill="var(--navy)"/>
      <path d="M0 70H220C245 70 250 56 280 56H580" fill="none" stroke="var(--green)" stroke-width="4"/>
    </svg>
    <div class="brand"><span class="brand__dot"></span>Corvel Poisson</div>
    <div class="carcass-bar"></div>
    <div class="title-bar carcass-title"><span class="title-bar__rule"></span>Tilapia Carcass</div>
    <div class="photo photo--carcass" role="img" aria-label="Photo of a tilapia carcass with head on a white plate"></div>
    <table class="pricing pricing--green">
      <thead>
        <tr><th class="cut" rowspan="2">CUT</th><th colspan="4">WEEKLY PRICING</th></tr>
        <tr><th>$/LB (1–50 lbs)</th><th>$/LB (51–150 lbs)</th><th>$/LB (151–250 lbs)</th><th>$/LB (+251 lbs)</th></tr>
      </thead>
      <tbody>
        <tr><th>Carcass (incl head)</th><td>0.50</td><td>0.45</td><td>0.43</td><td>0.40</td></tr>
      </tbody>
    </table>
    <svg class="band band--bottom" viewBox="0 0 580 90" aria-hidden="true">
      <path d="M0 90H580V28H280C250 28 245 14 220 14H0Z" fill="var(--navy)"/>
      <path d="M0 6H220C245 6 250 20 280 20H580" fill="none" stroke="var(--green)" stroke-width="4"/>
    </svg>
    <div class="folio"><span>509 2000 0147</span>
      <svg viewBox="0 0 24 24" aria-hidden="true"><circle cx="12" cy="12" r="11" fill="none" stroke="#fff" stroke-width="2"/><path d="M8 6l3 3-2 2c1 2 2 3 4 4l2-2 3 3-2 2C10 18 6 14 6 8z" fill="#fff"/></svg>
      <span>|&nbsp;&nbsp;7</span></div>
  </section>
</main>
</body>
</html>
```